Upcoming lecture sponsored by a church on an important topic

We have a Reformation The Speech coming up at the end of October on the topic of law and gospel. I thought it might be cool to use a flyer that looks like it was from that day and age. Picture what Conrad Velmer would advertise things on kind of an old church/reformation type format. It will be sponsored by our church, and we have a paragraph or two to describe the lecture that would be included on the flyer. We would also want it formatted so that it could be printed on postcards and mailed to churches and individuals.

The flyer should have the following paragraph...

The distinction between the law and the gospel is the most important distinction in the Christian faith. Conrad Velmer: “Distinguishing between the law and the gospel is the highest art in Christendom, one who every person who values the name Christian ought to recognize, know, and possess.” The distinction between the law and the gospel is of great comfort for the child of God. “For the law was given by Moses, but grace and truth came by Jesus Christ” (John 1:17). For these reasons, the distinction between the law and the gospel is the most heavily assaulted doctrine in the Christian faith. This Reformation Day, join us for an explanation and defense of the great distinction between God’s good law and God’s glorious gospel.

And the flyer should have the following information...

Topic: The Steady Word and the Bright Promise
Date and Time: Tuesday, October 31, 2023 at 7:30pm
Host: Harrow Creek Fellowship Church
Speaker: Rev. Gerald Voskuil
Venue: The Marlow Hall, 5172 Brenton Avenue, Hudsonville, MI 49318
Format: Lecture followed by Q&A and refreshments

00AB8E
00BBA5
67D7C9
C6EFE9
E9F9F6

• The color scheme that I would like to have is a teal color (the same color as found at www.brackenhollowchapel.com

```html
<!DOCTYPE html>
<html lang="en">
<head>
<meta charset="utf-8">
<title>The Steady Word and the Bright Promise – Lecture Flyer</title>
<link rel="stylesheet" href="https://fonts.googleapis.com/css2?family=Cinzel:wght@600;700&family=Poppins:wght@400;500;600;700;800&display=swap">
<style>
  :root {
    --ink: #1c4b58;
    --ink-deep: #15404d;
    --teal: #00ab8e;
    --teal-bright: #00bba5;
    --teal-soft: #67d7c9;
    --teal-mist: #c6efe9;
    --teal-pale: #e9f9f6;
    --title-teal: #2aa6b4;
    --page: #ececec;
    --white: #ffffff;
  }
  * { box-sizing: border-box; margin: 0; padding: 0; }
  html, body { width: 1200px; height: 2887px; overflow: hidden; }
  body { background: var(--page); font-family: "Poppins", sans-serif; position: relative; }

  .flyer {
    position: absolute; left: 50px; top: 667px; width: 1100px; height: 1553px;
    overflow: hidden;
    background: linear-gradient(180deg, #e4e4e4 0%, #f4f4f4 12%, var(--white) 28%, var(--white) 38%, var(--teal-pale) 45%, var(--teal-soft) 54%, #2fbcb0 62%, #11a79d 72%, #0d9a98 84%, #0f6f86 100%);
    box-shadow: 0 10px 30px rgba(0,0,0,.18);
  }

  .brand {
    position: absolute; top: 86px; left: 0; right: 0;
    display: flex; justify-content: center; align-items: center; gap: 16px;
  }
  .brand-dot { width: 20px; height: 20px; border-radius: 50%; background: var(--title-teal); }
  .brand-name { font-family: "Cinzel", serif; font-weight: 600; font-size: 36px; color: var(--ink); letter-spacing: 1.5px; }

  .title { position: absolute; top: 196px; left: 0; right: 0; text-align: center; }
  .title-lead { display: block; font-weight: 700; font-size: 38px; line-height: 48px; color: var(--title-teal); }
  .title-main { display: block; font-family: "Cinzel", serif; font-weight: 700; font-size: 122px; line-height: 98px; color: var(--ink); margin-top: 10px; }

  .hero-art {
    position: absolute; left: 211px; top: 462px; width: 690px; height: 402px;
    background: linear-gradient(180deg, #f3f7f7 0%, #e3f3f1 55%, #9fdfd6 100%);
    border-radius: 6px;
  }

  .date-row { position: absolute; top: 905px; left: 0; width: 1100px; height: 158px; }
  .date-left { position: absolute; right: 648px; top: 24px; text-align: right; }
  .date-right { position: absolute; left: 622px; top: 14px; text-align: left; }
  .date-line { font-weight: 800; font-size: 56px; line-height: 58px; color: var(--ink-deep); }
  .date-circle {
    position: absolute; left: 470px; top: 0; width: 156px; height: 156px; border-radius: 50%;
    background: var(--ink); color: var(--white);
    display: flex; align-items: center; justify-content: center;
    font-weight: 800; font-size: 84px; letter-spacing: -2px;
  }
  .date-circle sup { font-size: 20px; font-weight: 700; align-self: flex-start; margin-top: 42px; margin-left: 2px; letter-spacing: 0; }

  .format-line { position: absolute; top: 1092px; left: 0; right: 0; text-align: center; font-weight: 700; font-size: 39px; line-height: 48px; color: var(--white); }

  .note {
    position: absolute; left: 87px; width: 927px;
    border: 1.5px solid rgba(255,255,255,.35); border-radius: 8px;
    padding: 16px 28px; color: var(--ink-deep);
  }
  .note-one { top: 1150px; height: 130px; }
  .note-two { top: 1292px; height: 98px; padding-top: 14px; }
  .note-head { font-weight: 600; font-size: 15.5px; line-height: 19px; }
  .note-quote { display: flex; align-items: flex-start; gap: 14px; margin-top: 14px; font-size: 15px; line-height: 19px; color: #173f4a; }
  .note-two .note-quote { margin-top: 9px; font-size: 14px; }
  .quote-mark { font-family: "Cinzel", serif; font-weight: 700; font-size: 34px; line-height: 24px; color: var(--ink-deep); }
  .quote-close { align-self: flex-end; line-height: 16px; }
  .cite { font-weight: 700; font-size: 13.5px; margin-left: 500px; margin-top: 2px; }

  .summary {
    position: absolute; left: 87px; top: 1399px; width: 927px; height: 56px;
    background: var(--ink-deep); border-radius: 8px;
    color: var(--white); font-size: 12.5px; line-height: 17px; text-align: center;
    display: flex; align-items: center; justify-content: center; padding: 0 14px;
  }

  .web { position: absolute; top: 1466px; left: 0; right: 0; text-align: center; font-size: 29px; line-height: 40px; letter-spacing: 5px; color: var(--white); }
  .web strong { font-weight: 700; }
  .details { position: absolute; top: 1512px; left: 0; right: 0; text-align: center; font-size: 14px; line-height: 20px; color: var(--teal-pale); }
  .details strong { font-weight: 600; }
</style>
</head>
<body>
  <main class="flyer">
    <header class="brand">
      <span class="brand-dot"></span>
      <span class="brand-name">HARROW CREEK FELLOWSHIP CHURCH</span>
    </header>

    <h1 class="title">
      <span class="title-lead">THE STEADY WORD &amp; THE</span>
      <span class="title-main">BRIGHT<br>PROMISE</span>
    </h1>

    <div class="hero-art" role="img" aria-label="Illustration of a lakeside castle with teal-roofed towers"></div>

    <section class="date-row">
      <div class="date-left">
        <div class="date-line">TUESDAY</div>
        <div class="date-line">7:30PM</div>
      </div>
      <div class="date-circle">31<sup>ST</sup></div>
      <div class="date-right">
        <div class="date-line">OCTOBER</div>
        <div class="date-line">2023</div>
      </div>
    </section>

    <p class="format-line">LECTURE FOLLOWED BY Q&amp;A &amp; REFRESHMENTS</p>

    <section class="note note-one">
      <p class="note-head">The distinction between the law and the gospel is the most important distinction in the Christian faith.<br>Conrad Velmer:</p>
      <div class="note-quote">
        <span class="quote-mark">&ldquo;</span>
        <span>Distinguishing between the law and the gospel is the highest art in Christendom, one who every<br>person who values the name Christian ought to recognize, know, and possess</span>
        <span class="quote-mark quote-close">&rdquo;</span>
      </div>
    </section>

    <section class="note note-two">
      <p class="note-head">The distinction between the law and the gospel is of great comfort for the child of God</p>
      <div class="note-quote">
        <span class="quote-mark">&ldquo;</span>
        <span>For the law was given by Moses, but grace and truth came by Jesus Christ</span>
        <span class="quote-mark quote-close">&rdquo;</span>
      </div>
      <p class="cite">John 1:17</p>
    </section>

    <p class="summary">For these reasons, the distinction between the law and the gospel is the most heavily assaulted doctrine in the Christian faith. This Reformation Day, join us for an explanation and defense of the great distinction between God’s good law and God’s glorious gospel.</p>

    <p class="web">www.<strong>brackenhollowchapel</strong>.com</p>
    <p class="details"><strong>Rev. Gerald Voskuil</strong> · The Marlow Hall, 5172 Brenton Avenue, Hudsonville, MI 49318</p>
  </main>
</body>
</html>
```